Bride Basecamp

I am looking for a design for http://www.bridebasecamp.co.uk/ its a joomla site and I am going to set up with the same mods as our stag version http://www.groomnightout.co.uk/ you will see on groomnight how all the menus look and are positioned. Here is an example of a activity page http://www.groomnightout.co.uk/activity/white-water-rafting-in-perthshire.html which comes from Kiln.

The design needs to be built for responsive layout. The brand look and feel needs to be 100% for the female market.

We can accept the design in photoshop or something similar

Please ask questions if you require more information.

some examples of hen sites

http://www.maidenmerry.co.uk/

```html
<!DOCTYPE html>
<html lang="en">
<head>
<meta charset="utf-8">
<title>Bride Basecamp</title>
<link href="https://fonts.googleapis.com/css2?family=Open+Sans:ital,wght@0,400;0,600;1,400&display=swap" rel="stylesheet">
<style>
:root{
  --orange:#e8740c;
  --nav-dark:#1c1c1c;
  --nav-line:#3a3a3a;
  --text:#555;
  --heading:#333;
  --review-blue:#5a9be0;
  --star:#f3a10d;
  --footer:#2b2b2b;
  --footer-text:#e6e6e6;
  --tile-band:rgba(20,20,20,.55);
}
*{box-sizing:border-box;margin:0;padding:0}
html,body{width:899px;height:1200px;overflow:hidden;background:#fff}
body{position:relative;font-family:"Open Sans",Arial,sans-serif;color:var(--text)}
.top-rule{position:absolute;left:0;top:0;width:899px;height:1px;background:#e5e5e5}
.brand{position:absolute;left:128px;top:38px;display:flex;align-items:center;gap:8px;font-size:20px;font-weight:600;letter-spacing:.5px;color:var(--heading);text-transform:uppercase}
.brand-mark{width:12px;height:12px;background:var(--orange)}
.search{position:absolute;left:611px;top:44px;width:158px;height:20px;border:1px solid #cfcfcf;font-size:10px;color:#888;padding:3px 10px}
.search svg{position:absolute;right:6px;top:3px}
.main-nav{position:absolute;left:128px;top:88px;width:641px;height:36px;background:linear-gradient(#2a2a2a,#111);display:flex;border-radius:2px;overflow:hidden}
.main-nav a{display:flex;align-items:center;justify-content:center;color:#fff;text-decoration:none;font-size:12px;font-weight:600;text-transform:uppercase;border-right:1px solid var(--nav-line)}
.main-nav a:last-child{border-right:none}
.main-nav a.active{background:var(--orange)}
.hero{position:absolute;left:128px;top:130px;width:641px;height:257px;background:radial-gradient(circle at 25% 20%,#5aa4e8 0,#2a4c9a 25%,transparent 50%),radial-gradient(circle at 85% 25%,#e0409a 0,#7a2a80 30%,transparent 55%),linear-gradient(100deg,#2c1c3c,#b0603c 45%,#6a2a4a 70%,#2a1020)}
.hero-caption{position:absolute;left:0;top:193px;width:349px;height:39px;background:rgba(60,50,50,.7);color:#fff;font-family:Arial,sans-serif;font-size:19px;padding:8px 11px;letter-spacing:.2px}
.hero-dots{position:absolute;right:15px;bottom:11px;display:flex;gap:3px}
.hero-dots span{width:6px;height:6px;border-radius:50%;background:#333;border:1px solid #fff}
.hero-dots span:first-child{background:#fff}
h2.section-title{position:absolute;font-size:18px;font-weight:400;color:var(--orange)}
.welcome-title{left:128px;top:428px}
.welcome-copy{position:absolute;left:128px;top:462px;width:380px;font-size:9.6px;line-height:15px}
.welcome-copy p{margin-bottom:3px}
.video{position:absolute;left:543px;top:435px;width:226px;height:137px;background:#111;box-shadow:0 1px 3px rgba(0,0,0,.5)}
.video-frame{position:absolute;left:2px;top:2px;width:222px;height:118px;background:linear-gradient(110deg,#4a2a3a,#a06a5a 40%,#6a4a3a 60%,#3a2a30)}
.video-play{position:absolute;left:95px;top:42px}
.video-bar{position:absolute;left:8px;top:124px;width:210px;height:8px}
.tile{position:absolute;width:144px;height:125px;background:#fff;border:1px solid #e2e2e2;box-shadow:0 0 3px rgba(0,0,0,.15);padding:4px}
.tile-photo{position:relative;width:100%;height:100%}
.tile-label{position:absolute;left:0;bottom:0;width:100%;height:24px;background:var(--tile-band);color:#fff;font-size:12px;font-weight:600;padding:4px 9px}
.reviews-title{left:128px;top:938px}
.review{position:absolute;top:982px;width:130px;font-family:Arial,sans-serif}
.review h3{font-size:12px;font-weight:400;color:var(--review-blue)}
.stars{display:flex;gap:1px;margin:5px 0 6px}
.review p{font-size:9px;line-height:13.5px;color:#444}
.review cite{display:block;text-align:right;font-size:9px;color:#444;margin-top:5px}
.site-footer{position:absolute;left:0;top:1125px;width:899px;height:75px;background:var(--footer);font-family:Arial,sans-serif;color:var(--footer-text);font-size:9.5px}
.footer-links{position:absolute;left:135px;top:20px}
.copyright{position:absolute;left:135px;top:43px}
.social{position:absolute;left:647px;top:27px;display:flex;gap:9px}
.social span{width:22px;height:22px;border-radius:2px}
</style>
</head>
<body>
<div class="top-rule"></div>
<header>
  <div class="brand"><span class="brand-mark"></span>Bride Basecamp</div>
  <div class="search">Search
    <svg width="12" height="12" viewBox="0 0 12 12"><circle cx="4.5" cy="4.5" r="3.3" fill="none" stroke="#333" stroke-width="1.6"/><line x1="7" y1="7" x2="11" y2="11" stroke="#333" stroke-width="2"/></svg>
  </div>
  <nav class="main-nav">
    <a class="active" style="width:76px">Home</a>
    <a style="width:115px">Locations</a>
    <a style="width:190px">European Destinations</a>
    <a style="width:103px">Contact</a>
    <a style="width:157px">Call 0181 555 0142</a>
  </nav>
</header>

<section class="hero" role="img" aria-label="Photo of a group of women dancing at a party under colourful club lights">
  <div class="hero-caption">DUIS AUTEM VEL EUM IRURE DOLOR</div>
  <div class="hero-dots"><span></span><span></span><span></span><span></span></div>
</section>

<h2 class="section-title welcome-title">Welcome to Our Website</h2>
<div class="welcome-copy">
  <p>Eu tortor euismodolo. Vestibulum ant psu meop primis inicibu orci luctus eduluere cubil. Cura sed quis nibhut odiocinialor matis ed iaculis ante sed vel lacinieusmmodolo. Vestibi ulum ant psu meop primis inicibu orci luctus ed ultrices etpCiuraised quis nibhut odiocni alor matis ed iaculis ante sed vel laciniate.</p>
  <p>Eu tortor euismodolo. Vestibulum ant psu meop primis inicibu orci luctus eduluere cubil. Cura sed quis nibhut odiocinialor matis ed iaculis ante sed vel lacineusmmodolo. Vestibu lum ant psu meop primis inicibu orci luctus ed ultrices. Vestibulum ant psu meop primi in icibu orci luctus ed ultrices. Vestibulum ant psu meop primis inicibu.</p>
</div>

<div class="video">
  <div class="video-frame" role="img" aria-label="Video still of women celebrating at a hen party">
    <svg class="video-play" width="32" height="32" viewBox="0 0 32 32"><circle cx="16" cy="16" r="16" fill="rgba(255,255,255,.25)"/><path d="M12 8 L24 16 L12 24 Z" fill="rgba(255,255,255,.85)"/></svg>
  </div>
  <svg class="video-bar" width="210" height="8" viewBox="0 0 210 8">
    <path d="M0 1 L5 4 L0 7 Z" fill="#fff"/>
    <rect x="10" y="3" width="110" height="2" fill="#555"/>
    <rect x="10" y="3" width="50" height="2" fill="#d0202a"/>
    <text x="124" y="7" font-size="6" fill="#fff" font-family="Arial">1:26 / 3:22</text>
    <path d="M160 3 h2 l2 -2 v6 l-2 -2 h-2 Z" fill="#fff"/>
    <rect x="167" y="3" width="14" height="2" fill="#d0202a"/>
    <rect x="188" y="2" width="6" height="4" fill="none" stroke="#fff" stroke-width="1"/>
    <text x="198" y="7" font-size="6" font-weight="bold" fill="#fff" font-family="Arial">HD</text>
  </svg>
</div>

<section class="locations">
  <div class="tile" style="left:128px;top:622px"><div class="tile-photo" role="img" aria-label="Photo of green valley and hills" style="background:linear-gradient(#c8ccd0,#8a9a8a 35%,#4a7a30 55%,#2a5a20)"><span class="tile-label">Aviemore</span></div></div>
  <div class="tile" style="left:293px;top:622px"><div class="tile-photo" role="img" aria-label="Photo of an indoor pool with yellow water slides" style="background:linear-gradient(#e8ecef,#c8d4d8 35%,#d8c850 50%,#4aa0b8 70%,#2a7a98)"><span class="tile-label">Bournemouth</span></div></div>
  <div class="tile" style="left:461px;top:622px"><div class="tile-photo" role="img" aria-label="Photo of a steam train crossing moorland" style="background:linear-gradient(#9ab8d8,#7a8aa0 30%,#5a4a48 55%,#7a4a30 75%,#4a3020)"><span class="tile-label">Bristol</span></div></div>
  <div class="tile" style="left:625px;top:622px"><div class="tile-photo" role="img" aria-label="Photo of a snow-covered rock formation under blue sky" style="background:linear-gradient(#2a4a8a,#5a7ab0 40%,#c8d4e4 65%,#e8eef4)"><span class="tile-label">Silverdale</span></div></div>
  <div class="tile" style="left:128px;top:772px"><div class="tile-photo" role="img" aria-label="Photo of rows of vineyard vines" style="background:linear-gradient(#2a5a2a,#5a8a2a 30%,#c8b020 60%,#6a7a20)"><span class="tile-label">Manchestar</span></div></div>
  <div class="tile" style="left:293px;top:772px"><div class="tile-photo" role="img" aria-label="Photo of dancers in feathered costumes on stage" style="background:linear-gradient(#3a2a20,#8a5a3a 40%,#4a8aa0 70%,#2a3a40)"><span class="tile-label">Bournemouth</span></div></div>
  <div class="tile" style="left:461px;top:772px"><div class="tile-photo" role="img" aria-label="Photo of skiers on a snowy slope" style="background:linear-gradient(#8a8a8a,#c8c8c8 30%,#e8e8ec 55%,#d8dce4)"><span class="tile-label">Bristol</span></div></div>
  <div class="tile" style="left:625px;top:772px"><div class="tile-photo" role="img" aria-label="Photo of green fields under a cloudy sky" style="background:linear-gradient(#5a6068,#8a9098 35%,#4a6a50 55%,#6aa040 75%,#3a6a2a)"><span class="tile-label">Silverdale</span></div></div>
</section>

<h2 class="section-title reviews-title">Customer Reviews</h2>
<section class="reviews">
  <article class="review" style="left:128px"><h3>Very Good</h3>
    <div class="stars"><svg width="62" height="11" viewBox="0 0 62 11"><g fill="var(--star)"><path id="s" d="M5.5 0 L7 3.8 L11 4 L7.9 6.5 L9 10.5 L5.5 8.2 L2 10.5 L3.1 6.5 L0 4 L4 3.8 Z"/><use href="#s" x="12.5"/><use href="#s" x="25"/><use href="#s" x="37.5"/><use href="#s" x="50"/></g></svg></div>
    <p>Duis auteim vel eumirurer heniin putaite velit esse. Cliaritas eetim pcessus. consuetudium lectoum</p><cite>Lena Hart</cite></article>
  <article class="review" style="left:296px"><h3>Friendly and Helpfull</h3>
    <div class="stars"><svg width="62" height="11" viewBox="0 0 62 11"><g fill="var(--star)"><use href="#s"/><use href="#s" x="12.5"/><use href="#s" x="25"/><use href="#s" x="37.5"/><use href="#s" x="50"/></g></svg></div>
    <p>Duis auteim vel eumirurer heniin putaite velit esse. Cliaritas eetim pcessus. consuetudium lectoum</p><cite>Lena Hart</cite></article>
  <article class="review" style="left:469px"><h3>Friendly and Helpfull</h3>
    <div class="stars"><svg width="62" height="11" viewBox="0 0 62 11"><g fill="var(--star)"><use href="#s"/><use href="#s" x="12.5"/><use href="#s" x="25"/><use href="#s" x="37.5"/><use href="#s" x="50"/></g></svg></div>
    <p>Duis auteim vel eumirurer heniin putaite velit esse. Cliaritas eetim pcessus. consuetudium lectoum</p><cite>Lena Hart</cite></article>
  <article class="review" style="left:641px"><h3>Friendly and Helpfull</h3>
    <div class="stars"><svg width="62" height="11" viewBox="0 0 62 11"><g fill="var(--star)"><use href="#s"/><use href="#s" x="12.5"/><use href="#s" x="25"/><use href="#s" x="37.5"/><use href="#s" x="50"/></g></svg></div>
    <p>Duis auteim vel eumirurer heniin putaite velit esse. Cliaritas eetim pcessus. consuetudium lectoum</p><cite>Lena Hart</cite></article>
</section>

<footer class="site-footer">
  <div class="footer-links">Terms and Conditions | Privacy Promise | FAQ's | Contact Us</div>
  <div class="copyright">Copyright © 2013. All Rights Reserved.</div>
  <div class="social">
    <span style="background:#3b5ba8"></span>
    <span style="background:#2a9ad8"></span>
    <span style="background:#f07a1a"></span>
    <span style="background:#d8242a"></span>
  </div>
</footer>
</body>
</html>
```